Request for Business Card Design

Hi. My name is Marlena, I am looking for a new business card design for my company, Quorvane Sensing Systems, LLC. I really like the design you did for Tessaly Harvest and was hoping you could do something similar using our full logo and our mark. I am also open to any raised texture design using our mark. I have attached our full logo, which would need to be somewhere on the card, as well as the mark in both outline and full form, as well as our brand colors / guide. The card does not have to be white, as long as our logo and mark appear. I actually like darker colored business cards more, but am open to all options. If you are interested in working with me, please let me know. We would also take the business card design into letterhead design if you can do that.

```html
<!DOCTYPE html>
<html lang="en">
<head>
<meta charset="utf-8">
<title>Quorvane Sensing Systems – Business Card</title>
<link rel="stylesheet" href="https://fonts.googleapis.com/css2?family=Lato:wght@400;700;900&display=swap">
<style>
  :root {
    --backdrop: #2b2d30;
    --card-white: #ffffff;
    --card-dark: #3a3a3c;
    --ink: #2a2a2a;
    --ink-soft: #555555;
    --brand-blue: #1a9ac9;
    --faint: #efefef;
    --on-dark: #ffffff;
  }
  * { box-sizing: border-box; margin: 0; padding: 0; }
  html, body { width: 1200px; height: 952px; overflow: hidden; }
  body {
    background: var(--backdrop);
    font-family: "Lato", sans-serif;
    position: relative;
  }
  .card {
    position: absolute;
    top: 326px;
    width: 525px;
    height: 300px;
    border-radius: 24px;
    overflow: hidden;
  }
  .card--front { left: 45px; background: var(--card-white); color: var(--ink); }
  .card--back { left: 630px; background: var(--card-dark); color: var(--on-dark); }

  .faint-disc {
    position: absolute;
    left: 150px; top: 30px;
    width: 150px; height: 150px;
    border-radius: 50%;
    border: 26px solid var(--faint);
  }

  .person { position: absolute; left: 40px; top: 118px; }
  .person__name { font-size: 19px; font-weight: 400; letter-spacing: 1px; text-transform: uppercase; }
  .person__surname { color: var(--brand-blue); font-weight: 900; }
  .person__title { font-size: 14px; color: var(--ink-soft); margin-top: 6px; padding-left: 40px; }

  .brand { position: absolute; display: flex; align-items: center; gap: 12px; }
  .brand__dot { width: 14px; height: 14px; border-radius: 50%; background: var(--brand-blue); flex: none; }
  .brand__text { font-weight: 900; text-transform: uppercase; line-height: 1; }
  .brand__name { font-size: 34px; letter-spacing: 3px; }
  .brand__tag { font-size: 10.5px; letter-spacing: 1px; margin-top: 4px; }
  .card--front .brand { left: 292px; top: 112px; }
  .card--front .brand__name { font-size: 30px; }
  .card--back .brand { left: 118px; top: 118px; }

  .contacts { position: absolute; left: 272px; top: 182px; list-style: none; font-size: 11.5px; color: var(--ink-soft); }
  .contacts li { display: flex; align-items: flex-start; gap: 8px; margin-bottom: 6px; line-height: 1.3; }
  .contacts svg { width: 14px; height: 14px; flex: none; margin-top: 1px; }
</style>
</head>
<body>
  <section class="card card--front" aria-label="Card front">
    <div class="faint-disc" aria-hidden="true"></div>
    <div class="person">
      <p class="person__name">Dorian K. <span class="person__surname">Whitcombe</span></p>
      <p class="person__title">Managing Director</p>
    </div>
    <div class="brand">
      <div class="brand__text">
        <p class="brand__name">Quorvane</p>
        <p class="brand__tag">Sensing Systems</p>
      </div>
    </div>
    <ul class="contacts">
      <li>
        <svg viewBox="0 0 14 14" aria-hidden="true"><rect width="14" height="14" rx="2" fill="#2a2a2a"/><path d="M7 3a2.6 2.6 0 0 0-2.6 2.6C4.4 8 7 11 7 11s2.6-3 2.6-5.4A2.6 2.6 0 0 0 7 3z" fill="#fff"/><circle cx="7" cy="5.6" r="1" fill="#2a2a2a"/></svg>
        <span>1720 Halden Avenue<br>Arlington, VA 22201</span>
      </li>
      <li>
        <svg viewBox="0 0 14 14" aria-hidden="true"><rect width="14" height="14" rx="2" fill="#1a9ac9"/><path d="M4.5 3.5l1.6-.2.8 2-1 .8a5 5 0 0 0 2 2l.8-1 2 .8-.2 1.6c-3.5.3-6.3-2.5-6-6z" fill="#fff"/></svg>
        <span>+00 481 927 35</span>
      </li>
      <li>
        <svg viewBox="0 0 14 14" aria-hidden="true"><rect width="14" height="14" rx="2" fill="#1a9ac9"/><rect x="3" y="4.2" width="8" height="5.6" fill="none" stroke="#fff" stroke-width="1"/><path d="M3 4.2l4 3 4-3" fill="none" stroke="#fff" stroke-width="1"/></svg>
        <span>hello@quorvane.com</span>
      </li>
      <li>
        <svg viewBox="0 0 14 14" aria-hidden="true"><rect width="14" height="14" rx="2" fill="#1a9ac9"/><path d="M4.5 3.5l5.5 3-2.3.7 1.6 2.5-1 .6-1.5-2.5-1.7 1.6z" fill="#fff"/></svg>
        <span>www.quorvane.com</span>
      </li>
    </ul>
  </section>

  <section class="card card--back" aria-label="Card back">
    <div class="brand">
      <span class="brand__dot" aria-hidden="true"></span>
      <div class="brand__text">
        <p class="brand__name">Quorvane</p>
        <p class="brand__tag">Sensing Systems</p>
      </div>
    </div>
  </section>
</body>
</html>
```